Website for premium health insurance and concierge medicine

This is a brand new website for Vantor Insurance Services that specializes in Health Insurance and Concierge Medicine for high net-worth and affluent individuals and families. Through this website, clients will be able to learn about products and services, submit applications, and complete self enrollment forms. The website needs to have a premium look & feel that will appeal to a discerning high net-worth individual.

I’m looking for 4 pages in total to begin with. I’m also looking for a designer who will be interested in continuing to build out this new site further over the next few months.

The headline for each page is listed below:

Page 1: HOME PAGE
“Premium Healthcare | Bespoke Concierge Services | Absolute Peace of Mind.”

Page 2: HEALTH INSURANCE
“Premium Healthcare | Elevated.”

Page 3: CONCIERGE MEDICINE
“Personalized Medicine | At-Home Concierge Care | Your Private Physician, 24/7.”

Page 4: DENTAL & VISION
“Your Smile | Your Vision | Perfected.”

Here are several links to existing websites that can be used as design inspiration:

https://brevanwell.com
https://www.quemby.org/specialties-services/other-programs-services/concierge-medicine
https://physelmdkx.com

More generally speaking, I like a clean, modern, dutch style of websites. Here’s an unrelated site that has a good design:

https://www.ostravine.com

Here are a few additional phrases and keywords that will help inspire the design:

Premium Health Insurance
Executive Health Insurance
Concierge Medicine
24/7 access dedicated concierge team
Integrative Concierge Care

I will upload logo files below, here are the font & colors information:

Font: Trajan Pro Bold
Colors:
Blue: hex code: 0071BD, Rgb code: 0, 113, 189  cmyk code: 87,53,0,0
Gray: hex code: #666666, Rgb code: 102,102,102 cmyk code: 60,51,51,20

```html
<!DOCTYPE html>
<html lang="en">
<head>
<meta charset="utf-8">
<title>Vantor Insurance Services – Premium Healthcare & Concierge Medicine</title>
<link href="https://fonts.googleapis.com/css2?family=Cinzel:wght@400;600;700&family=Inter:wght@400;500;600;700&display=swap" rel="stylesheet">
<style>
:root{
  --blue:#0071BD;
  --blue-dark:#005fa3;
  --blue-mid:#0a6ab3;
  --gray:#666666;
  --ink:#333333;
  --sky:#e2f2fc;
  --sky-2:#eef7fd;
  --paper:#f4f5f6;
  --dark:#2a2a2a;
  --darker:#3a3a3a;
  --star:#f5b400;
  --white:#ffffff;
}
*{margin:0;padding:0;box-sizing:border-box}
html,body{width:1200px;height:3250px;overflow:hidden}
body{font-family:"Inter",Arial,sans-serif;color:var(--ink);background:var(--white);font-size:12px}
section,header,footer{position:relative;width:1200px}
svg{display:block}

/* top bar */
.topbar{height:33px;background:var(--gray);color:var(--white);display:flex;align-items:center;justify-content:space-between;padding:0 92px 0 94px;font-size:11px}
.topbar .contact{display:flex;gap:18px;align-items:center}
.topbar .contact span{display:flex;align-items:center;gap:6px}
.social{display:flex;gap:12px}
.social i{width:11px;height:11px;border-radius:50%;background:rgba(255,255,255,.9);display:block}

/* hero */
.hero{height:583px;background:linear-gradient(90deg,#dff0fb 0%,#e6f4fd 55%,#dcefff 100%)}
.nav{position:absolute;top:0;left:0;width:1200px;height:100px;display:flex;align-items:center;padding:0 92px;z-index:3}
.brand{display:flex;align-items:center;gap:10px;width:200px}
.brand .mark{width:18px;height:18px;border-radius:50%;background:var(--blue);flex:none}
.brand .name{font-family:"Cinzel",serif;font-weight:700;font-size:14px;color:var(--blue);line-height:1.15;width:140px}
.menu{display:flex;gap:21px;margin-left:5px;font-size:11px;font-weight:600;color:#444;letter-spacing:.2px}
.menu .active{color:var(--blue)}
.btn{display:inline-flex;align-items:center;justify-content:center;gap:8px;border-radius:18px;font-family:"Cinzel",serif;font-weight:600;font-size:13px;color:var(--white);background:var(--blue)}
.nav .btn{margin-left:auto;width:171px;height:33px}
.hero h1{position:absolute;left:90px;top:194px;width:560px;font-family:"Cinzel",serif;font-weight:600;font-size:31px;line-height:39px;color:var(--blue-dark);letter-spacing:0;z-index:2;white-space:nowrap}
.hero .lead{position:absolute;left:93px;top:326px;font-size:12.5px;line-height:20px;color:#444}
.hero .ctas{position:absolute;left:93px;top:385px;display:flex;gap:21px}
.hero .ctas .btn{width:171px;height:32px}
.btn.gray{background:var(--gray)}
.trust{position:absolute;left:94px;top:482px;display:flex;align-items:center;gap:14px}
.stars{display:flex;gap:4px}
.avatars{display:flex}
.avatars i{width:30px;height:30px;border-radius:50%;border:2px solid #fff;margin-left:-8px;background:linear-gradient(135deg,#c9b8a6,#6b7d92)}
.avatars i:first-child{margin-left:0}
.trust-label{position:absolute;left:94px;top:528px;font-size:10px;font-weight:700;color:var(--blue)}
.hero-photo{position:absolute;left:668px;top:128px;width:442px;height:468px;border-radius:40px 40px 50% 50% / 40px 40px 30% 30%;background:linear-gradient(160deg,#bcdcf3 0%,#d9c2a8 45%,#4f6f9a 100%);opacity:.95}
.hero-photo-frame{position:absolute;left:668px;top:128px;width:442px;height:468px;border:16px solid #9fcbec;border-radius:40px 40px 50% 50% / 40px 40px 30% 30%;opacity:.7}

/* features */
.features{height:145px;background:var(--blue);display:flex;color:var(--white)}
.feature{flex:1;display:flex;gap:14px;padding:38px 0 0 94px}
.feature.mid{background:var(--blue-mid);padding-left:48px}
.feature:last-child{padding-left:34px}
.feature h3{font-family:"Cinzel",serif;font-weight:600;font-size:16px;letter-spacing:.4px;margin-bottom:10px}
.feature p{font-size:11px;line-height:18px}

/* redefining */
.redefine{height:384px;background:var(--paper);text-align:center}
.eyebrow{display:flex;align-items:center;justify-content:center;gap:22px;font-family:"Cinzel",serif;font-size:20px;color:#555}
.eyebrow::before,.eyebrow::after{content:"";width:100px;height:1px;background:var(--blue);opacity:.6}
.section-title{font-family:"Cinzel",serif;font-weight:600;font-size:24px;color:var(--blue);letter-spacing:.4px;margin-top:6px}
.redefine .eyebrow{padding-top:70px}
.redefine .body{font-size:11.5px;line-height:19px;color:var(--gray);width:620px;margin:24px auto 0}
.redefine .tag{font-family:"Cinzel",serif;font-size:19px;color:var(--blue);margin-top:28px}
.redefine .btn{width:147px;height:32px;margin-top:24px}

/* services */
.services{height:569px;background:var(--sky-2);text-align:center}
.services .eyebrow{padding-top:58px}
.services .intro{font-size:11.5px;line-height:19px;color:#444;margin-top:18px}
.services .intro em{font-style:normal;color:var(--blue)}
.cards{display:flex;justify-content:center;gap:0;margin-top:22px}
.card{width:300px}
.shield{width:180px;height:198px;margin:0 auto;background:var(--blue);clip-path:polygon(0 6%,50% 0,100% 6%,100% 62%,50% 100%,0 62%);padding:4px}
.shield div{width:100%;height:100%;clip-path:polygon(0 6%,50% 0,100% 6%,100% 62%,50% 100%,0 62%)}
.card h3{font-family:"Cinzel",serif;font-weight:600;font-size:16px;color:var(--blue);margin-top:22px;letter-spacing:.5px}
.card p{font-size:10.5px;line-height:17px;color:var(--gray);margin-top:8px}
.card .btn{width:124px;height:28px;margin-top:14px;font-size:12px}

/* why */
.why{height:612px;background:var(--blue);color:var(--white)}
.why .eyebrow{padding-top:62px;color:#1a3550}
.why .eyebrow::before,.why .eyebrow::after{background:#fff;opacity:.5}
.why .section-title{color:var(--white)}
.why-left{position:absolute;left:128px;top:178px;width:500px}
.why-left h3{font-family:"Cinzel",serif;font-weight:600;font-size:20px;letter-spacing:.4px}
.why-left .p{font-size:11px;line-height:19.5px;margin-top:14px}
.why-list{list-style:none;margin-top:18px}
.why-list li{display:flex;gap:12px;font-size:11.5px;line-height:19px;margin-bottom:15px}
.why-list b{font-weight:500;color:#0f2e4d}
.why-left .btn{border:2px solid #fff;background:transparent;width:175px;height:38px;margin-top:8px;font-size:13px}
.collage-big{position:absolute;left:736px;top:171px;width:322px;height:336px;border:4px solid #fff;border-radius:14px;background:linear-gradient(160deg,#6f8c5e 0%,#c2a487 50%,#8a3a3f 100%)}
.collage-small{position:absolute;left:677px;top:387px;width:176px;height:166px;border:4px solid #fff;border-radius:12px;background:linear-gradient(150deg,#e9e2d6 0%,#e3c240 55%,#4a5568 100%)}
.badge{position:absolute;left:902px;top:392px;width:128px;height:124px;border:4px solid #fff;border-radius:14px;background:var(--blue);text-align:center;padding-top:12px}
.badge .num{font-size:38px;font-weight:700;line-height:40px;margin-top:4px}
.badge .lbl{font-size:9px;line-height:12px}

/* testimonials */
.testimonials{height:507px;background:var(--sky)}
.testimonials .eyebrow{padding-top:56px;text-align:center}
.testimonials .section-title{text-align:center}
.tcards{position:absolute;top:168px;left:93px;display:flex;gap:37px}
.tcard{width:316px;height:200px;background:var(--sky-2);border-radius:10px;box-shadow:0 3px 10px rgba(0,60,110,.14);padding:32px 0 0 34px;position:relative}
.tcard .photo{width:75px;height:75px;border:2px solid var(--blue);background:linear-gradient(150deg,#d9dde2,#7a8594)}
.tcard .quote{position:absolute;left:88px;top:22px;width:30px;height:30px;border-radius:50%;background:var(--blue);color:#fff;font-size:22px;font-weight:700;text-align:center;line-height:36px}
.tcard .who{position:absolute;left:138px;top:38px}
.tcard .who .stars{gap:2px}
.tcard .name{font-size:14px;font-weight:500;color:#333;margin-top:12px;letter-spacing:.4px}
.tcard .role{font-size:10px;color:var(--blue);margin-top:6px}
.tcard .txt{font-size:10px;line-height:16px;color:var(--gray);margin-top:20px;width:255px}

/* cta */
.cta{position:absolute;left:94px;top:2757px;width:1016px;height:143px;background:var(--blue);border-radius:12px;color:#fff;z-index:2}
.cta h2{position:absolute;left:59px;top:32px;font-family:"Cinzel",serif;font-weight:600;font-size:20px;line-height:25px;letter-spacing:.4px}
.cta p{position:absolute;left:58px;top:100px;font-size:12px}
.cta .btn{position:absolute;top:49px;height:42px;font-size:12px;border:2px solid #fff}
.cta .b1{left:558px;width:224px;background:transparent}
.cta .b2{left:795px;width:167px;background:var(--gray)}

/* footer */
.footer{height:372px;background:var(--dark);color:#fff}
.fcol{position:absolute;top:2950px;color:#fff}
.fcol h4{font-size:13px;font-weight:700;color:var(--blue);letter-spacing:.3px}
.fcol h4::after{content:"";display:block;width:120px;height:1px;background:#555;margin-top:8px}
.fcol ul{list-style:none;margin-top:18px}
.fcol li{font-size:10.5px;margin-bottom:19px;letter-spacing:.3px}
.fbrand{position:absolute;left:94px;top:2940px;color:#fff}
.fbrand .tagline{font-size:10.5px;line-height:17px;margin-top:40px}
.fbrand h5{font-size:13px;font-weight:700;color:var(--blue);margin-top:12px}
.fbrand .hours{font-size:10.5px;line-height:22px;margin-top:8px}
.info{display:flex;gap:14px;align-items:center;margin-bottom:18px;font-size:10.5px;line-height:17px}
.info .ic{width:30px;height:30px;border-radius:50%;background:#555;display:flex;align-items:center;justify-content:center;flex:none}
.bottombar{position:absolute;top:3205px;left:0;width:1200px;height:45px;background:var(--darker);color:#fff;font-size:10px;display:flex;align-items:center;justify-content:space-between;padding:0 115px 0 94px}
.bottombar nav{display:flex;gap:14px}
</style>
</head>
<body>

<div class="topbar">
  <div class="contact">
    <span><svg width="11" height="11" viewBox="0 0 12 12"><rect x="1" y="2.5" width="10" height="7" rx="1" fill="none" stroke="#fff"/><path d="M1 3l5 3.5L11 3" fill="none" stroke="#fff"/></svg>help@vantorinsuranceservice.com</span>
    <span><svg width="11" height="11" viewBox="0 0 12 12"><path d="M3 1l2 3-1.2 1.2a6 6 0 003 3L8 7l3 2-1 2C5 11 1 7 1 2z" fill="#fff"/></svg>+100-555-0142</span>
  </div>
  <div class="social"><i></i><i></i><i></i><i></i><i></i></div>
</div>

<header class="hero">
  <div class="nav">
    <div class="brand"><span class="mark"></span><span class="name">Vantor Insurance Services</span></div>
    <nav class="menu">
      <span class="active">HOME</span><span>HEALTH INSURANCE</span><span>CONCIERGE MEDICINE</span><span>DENTAL &amp; VISION</span><span>ABOUT</span><span>CONTACT</span>
    </nav>
    <span class="btn"><svg width="14" height="14" viewBox="0 0 14 14"><path d="M13 1L1 6l5 2 2 5z" fill="none" stroke="#fff" stroke-width="1.2"/></svg>GET A QUOTE</span>
  </div>

  <div class="hero-photo" role="img" aria-label="Smiling family of three sitting together on the floor in denim"></div>
  <div class="hero-photo-frame"></div>

  <h1>PREMIUM HEALTHCARE<br>BESPOKE CONCIERGE SERVICES<br>ABSOLUTE PEACE OF MIND</h1>
  <p class="lead">Exclusive health solutions for high-net-worth individuals &amp; families.<br>Get <b>24/7</b> access to world-class concierge medicine and premium insurance plans.</p>
  <div class="ctas">
    <span class="btn gray"><svg width="13" height="13" viewBox="0 0 12 12"><path d="M3 1l2 3-1.2 1.2a6 6 0 003 3L8 7l3 2-1 2C5 11 1 7 1 2z" fill="none" stroke="#fff"/></svg>+100-555-0142</span>
    <span class="btn"><svg width="14" height="14" viewBox="0 0 14 14"><path d="M13 1L1 6l5 2 2 5z" fill="none" stroke="#fff" stroke-width="1.2"/></svg>GET A QUOTE</span>
  </div>
  <div class="trust">
    <div class="stars">
      <svg width="16" height="16" viewBox="0 0 20 20"><path d="M10 1l2.7 5.6 6.1.9-4.4 4.3 1 6.1L10 15l-5.4 2.9 1-6.1L1.2 7.5l6.1-.9z" fill="#f5b400"/></svg>
      <svg width="16" height="16" viewBox="0 0 20 20"><path d="M10 1l2.7 5.6 6.1.9-4.4 4.3 1 6.1L10 15l-5.4 2.9 1-6.1L1.2 7.5l6.1-.9z" fill="#f5b400"/></svg>
      <svg width="16" height="16" viewBox="0 0 20 20"><path d="M10 1l2.7 5.6 6.1.9-4.4 4.3 1 6.1L10 15l-5.4 2.9 1-6.1L1.2 7.5l6.1-.9z" fill="#f5b400"/></svg>
      <svg width="16" height="16" viewBox="0 0 20 20"><path d="M10 1l2.7 5.6 6.1.9-4.4 4.3 1 6.1L10 15l-5.4 2.9 1-6.1L1.2 7.5l6.1-.9z" fill="#f5b400"/></svg>
      <svg width="16" height="16" viewBox="0 0 20 20"><path d="M10 1l2.7 5.6 6.1.9-4.4 4.3 1 6.1L10 15l-5.4 2.9 1-6.1L1.2 7.5l6.1-.9z" fill="none" stroke="#f5b400" stroke-width="1.5"/></svg>
    </div>
    <div class="avatars" role="img" aria-label="Small portraits of satisfied clients"><i></i><i></i><i></i><i></i></div>
  </div>
  <p class="trust-label">TRUSTED BY EXECUTIVES, BUSINESS OWNERS &amp; HIGH-NET-WORTH FAMILIES</p>
</header>

<section class="features">
  <div class="feature">
    <svg width="30" height="30" viewBox="0 0 30 30"><path d="M3 15a12 12 0 0124 0c-2-2-4-2-6 0-2-2-4-2-6 0-2-2-4-2-6 0-2-2-4-2-6 0z" fill="none" stroke="#fff" stroke-width="1.4"/><path d="M15 15v9a2.5 2.5 0 01-5 0" fill="none" stroke="#fff" stroke-width="1.4"/></svg>
    <div><h3>COMPREHENSIVE COVERAGE</h3><p>Protects against <b>12,600+ injuries &amp; illnesses</b>—<br>from minor accidents to critical conditions.</p></div>
  </div>
  <div class="feature mid">
    <svg width="32" height="32" viewBox="0 0 32 32"><path d="M27 14a12 12 0 11-6-9" fill="none" stroke="#fff" stroke-width="1.6"/><path d="M10 15l5 5L28 6" fill="none" stroke="#fff" stroke-width="1.8"/></svg>
    <div><h3>SEAMLESS &amp; HASSLE-FREE</h3><p>One simple, all-in-one plan with instant<br>digital access &amp; paperless admin tools.</p></div>
  </div>
  <div class="feature">
    <svg width="32" height="32" viewBox="0 0 32 32"><rect x="3" y="8" width="24" height="20" rx="2" fill="none" stroke="#fff" stroke-width="1.4"/><rect x="12" y="3" width="16" height="12" rx="1" fill="none" stroke="#fff" stroke-width="1.4"/><path d="M7 20h8M7 24h12M16 7h8M16 10h6" stroke="#fff" stroke-width="1.2"/></svg>
    <div><h3>FAST &amp; RELIABLE BENEFITS</h3><p>Claims processed <b>in hours, not weeks,</b><br>ensuring peace of mind when it matters most.</p></div>
  </div>
</section>

<section class="redefine">
  <div class="eyebrow">REDEFINING</div>
  <h2 class="section-title">PREMIUM HEALTHCARE &amp; CONCIERGE MEDICINE</h2>
  <p class="body">At <span style="color:#333">Vantor Insurance Services</span>, we provide elite health insurance and concierge medicine for high-net-worth individuals. Our white-glove service ensures <span style="color:#333">24/7 access to private physicians</span>, tailored insurance plans, and seamless healthcare management—all designed for those who demand the best.</p>
  <p class="tag">EXCLUSIVE. PERSONALIZED. STRESS-FREE.</p>
  <span class="btn">LEARN MORE</span>
</section>

<section class="services">
  <div class="eyebrow">OUR SERVICES</div>
  <h2 class="section-title">COMPREHENSIVE HEALTHCARE, TAILORED FOR YOU</h2>
  <p class="intro">Vantor Insurance Services <em>we specialize in</em> premium, personalized healthcare solutions<br><em>designed for discerning individuals.</em></p>
  <div class="cards">
    <div class="card">
      <div class="shield"><div role="img" aria-label="Multi-generation family smiling outdoors" style="background:linear-gradient(160deg,#8fb07a,#d9b9a4 55%,#7b5a4e)"></div></div>
      <h3>HEALTH INSURANCE</h3>
      <p>Elite coverage with top-tier hospitals and specialists<br>worldwide. No compromises, just peace of mind.</p>
      <span class="btn">READ MORE</span>
    </div>
    <div class="card">
      <div class="shield"><div role="img" aria-label="Doctor attending to a senior patient in a clinic" style="background:linear-gradient(160deg,#6b6b6b,#e7e4e0 50%,#3c4a5e)"></div></div>
      <h3>CONCIERGE MEDICINE</h3>
      <p>24/7 direct access to private physicians, on-demand<br>care, and VIP medical services at your convenience</p>
      <span class="btn">READ MORE</span>
    </div>
    <div class="card">
      <div class="shield"><div role="img" aria-label="Patient consulting a dental and vision specialist" style="background:linear-gradient(160deg,#d8d4cc,#b7484f 55%,#e8e6e2)"></div></div>
      <h3>DENTAL &amp; VISION PLANS</h3>
      <p>Comprehensive plans to ensure your smile and<br>vision stay flawless, with premium providers.</p>
      <span class="btn">READ MORE</span>
    </div>
  </div>
</section>

<section class="why">
  <div class="eyebrow">WHY CHOOSE US</div>
  <h2 class="section-title" style="text-align:center">THE VANTOR INSURANCE DIFFERENCE</h2>
  <div class="why-left">
    <h3>TRUSTED. SECURE. TAILORED FOR YOU.</h3>
    <p class="p">At Vantor Insurance Services, we specialize in providing elite healthcare solutions for<br>high-net-worth individuals, ensuring unmatched coverage and concierge care.<br>With our expertise, you gain:</p>
    <ul class="why-list">
      <li><svg width="18" height="20" viewBox="0 0 18 20"><path d="M9 1l7 3v6c0 4-3 7-7 9-4-2-7-5-7-9V4z" fill="none" stroke="#fff" stroke-width="1.2"/><path d="M5.5 10l2.5 2.5 4.5-5" fill="none" stroke="#fff" stroke-width="1.3"/></svg><span><b>Exclusive Access</b> – Premium health insurance &amp; concierge medical plans tailored<br>for executives &amp; affluent families.</span></li>
      <li><svg width="18" height="20" viewBox="0 0 18 20"><path d="M9 1l7 3v6c0 4-3 7-7 9-4-2-7-5-7-9V4z" fill="none" stroke="#fff" stroke-width="1.2"/><path d="M5.5 10l2.5 2.5 4.5-5" fill="none" stroke="#fff" stroke-width="1.3"/></svg><span><b>Personalized Service</b> – White-glove assistance with dedicated advisors ensuring<br>a seamless experience.</span></li>
      <li><svg width="18" height="20" viewBox="0 0 18 20"><path d="M9 1l7 3v6c0 4-3 7-7 9-4-2-7-5-7-9V4z" fill="none" stroke="#fff" stroke-width="1.2"/><path d="M5.5 10l2.5 2.5 4.5-5" fill="none" stroke="#fff" stroke-width="1.3"/></svg><span><b>Global Coverage</b> – Top-tier hospitals, specialists, and VIP medical services at<br>your fingertips.</span></li>
      <li><svg width="18" height="20" viewBox="0 0 18 20"><path d="M9 1l7 3v6c0 4-3 7-7 9-4-2-7-5-7-9V4z" fill="none" stroke="#fff" stroke-width="1.2"/><path d="M5.5 10l2.5 2.5 4.5-5" fill="none" stroke="#fff" stroke-width="1.3"/></svg><span><b>Trusted &amp; Secure</b> – Decades of experience in premium insurance &amp; concierge<br>healthcare solutions.</span></li>
    </ul>
    <span class="btn"><svg width="14" height="14" viewBox="0 0 14 14"><path d="M13 1L1 6l5 2 2 5z" fill="none" stroke="#fff" stroke-width="1.2"/></svg>GET A QUOTE</span>
  </div>
  <div class="collage-big" role="img" aria-label="Family of four smiling together outdoors among trees"></div>
  <div class="collage-small" role="img" aria-label="Parents and child sitting together on a sofa"></div>
  <div class="badge">
    <svg width="22" height="24" viewBox="0 0 22 24" style="margin:0 auto"><circle cx="11" cy="9" r="7" fill="none" stroke="#fff" stroke-width="1.2"/><circle cx="11" cy="9" r="3.5" fill="none" stroke="#fff"/><path d="M7 15l-2 8 6-3 6 3-2-8" fill="none" stroke="#fff" stroke-width="1.2"/></svg>
    <div class="num">20</div>
    <div class="lbl">YEARS OF<br>EXPERIENCES</div>
  </div>
</section>

<section class="testimonials">
  <div class="eyebrow">TESTIMONIALS</div>
  <h2 class="section-title">REAL STORIES, REAL CARE</h2>
  <div class="tcards">
    <div class="tcard">
      <div class="photo" role="img" aria-label="Portrait of client in a light suit"></div>
      <div class="quote">”</div>
      <div class="who">
        <div class="stars"><svg width="72" height="13" viewBox="0 0 100 18"><g fill="#f5b400"><path id="s" d="M9 0l2.4 5.5 6 .5-4.6 4 1.4 6L9 13l-5.2 3 1.4-6L.6 6l6-.5z"/><use href="#s" x="20"/><use href="#s" x="40"/><use href="#s" x="60"/><use href="#s" x="80"/></g></svg></div>
        <div class="name">ADRIAN K.</div>
        <div class="role">ENTREPRENEUR</div>
      </div>
      <p class="txt">Exceptional service! The concierge healthcare plan gave me 24/7 access to top specialists. Truly a game-changer</p>
    </div>
    <div class="tcard">
      <div class="photo" role="img" aria-label="Portrait of client in a dark blazer"></div>
      <div class="quote">”</div>
      <div class="who">
        <div class="stars"><svg width="72" height="13" viewBox="0 0 100 18"><g fill="#f5b400"><use href="#s"/><use href="#s" x="20"/><use href="#s" x="40"/><use href="#s" x="60"/><use href="#s" x="80"/></g></svg></div>
        <div class="name">ELENA M.</div>
        <div class="role">BUSINESS OWNER</div>
      </div>
      <p class="txt">Their white-glove approach made all the difference. I feel secure knowing my family's health is in the best hands</p>
    </div>
    <div class="tcard">
      <div class="photo" role="img" aria-label="Portrait of client wearing glasses"></div>
      <div class="quote">”</div>
      <div class="who">
        <div class="stars"><svg width="72" height="13" viewBox="0 0 100 18"><g fill="#f5b400"><use href="#s"/><use href="#s" x="20"/><use href="#s" x="40"/><use href="#s" x="60"/><use href="#s" x="80"/></g></svg></div>
        <div class="name">MARCUS T</div>
        <div class="role">PRIVATE EQUITY EXECUTIVE</div>
      </div>
      <p class="txt">From insurance to personalized care, everything is seamless. The best decision I've made for my well-being.</p>
    </div>
  </div>
</section>

<div class="cta">
  <h2>EXPERIENCE ELITE HEALTHCARE<br>LIKE NEVER BEFORE</h2>
  <p>Secure world-class healthcare solutions for you and your family</p>
  <span class="btn b1"><svg width="13" height="13" viewBox="0 0 12 12"><path d="M3 1l2 3-1.2 1.2a6 6 0 003 3L8 7l3 2-1 2C5 11 1 7 1 2z" fill="none" stroke="#fff"/></svg>BOOK A CONSULTATION</span>
  <span class="btn b2"><svg width="14" height="12" viewBox="0 0 14 12"><rect x="1" y="1.5" width="12" height="9" rx="1" fill="none" stroke="#fff"/><path d="M1 2l6 4.5L13 2" fill="none" stroke="#fff"/></svg>GET A QUOTE</span>
</div>

<footer class="footer"></footer>

<div class="fbrand">
  <div class="brand"><span class="mark"></span><span class="name">Vantor Insurance Services</span></div>
  <p class="tagline">Premium Insurance &amp; Concierge<br>Medicine Solutions</p>
  <h5>OPENING HOURS</h5>
  <p class="hours">MON - FRI 8:00 AM - 6:00 PM<br>SATURDAY 9:00 AM - 5:00 PM<br>SUNDAY CLOSED</p>
</div>
<div class="fcol" style="left:421px">
  <h4>EXPLORE</h4>
  <ul><li>COMPANY PROFILE</li><li>ABOUT</li><li>HELP CENTER</li><li>NEWS &amp; MEDIA</li><li>CONTACT</li></ul>
</div>
<div class="fcol" style="left:633px">
  <h4>OUR SERVICES</h4>
  <ul><li>HEALTH INSURANCE</li><li>CONCIERGE MEDICINE</li><li>DENTAL &amp; VISION PLANS</li></ul>
</div>
<div class="fcol" style="left:871px">
  <h4>CONTACT INFO</h4>
  <div style="margin-top:18px">
    <div class="info"><span class="ic"><svg width="12" height="14" viewBox="0 0 12 14"><path d="M6 13s5-5 5-8A5 5 0 001 5c0 3 5 8 5 8z" fill="#fff"/><circle cx="6" cy="5" r="1.8" fill="#555"/></svg></span><span>48 Larkmoor Street, Suite 210 Halden,<br>HL 40917</span></div>
    <div class="info"><span class="ic"><svg width="12" height="12" viewBox="0 0 12 12"><path d="M3 1l2 3-1.2 1.2a6 6 0 003 3L8 7l3 2-1 2C5 11 1 7 1 2z" fill="#fff"/></svg></span><span>+100 55501877<br>+100 55501933</span></div>
    <div class="info"><span class="ic"><svg width="12" height="10" viewBox="0 0 12 10"><rect x=".5" y=".5" width="11" height="9" rx="1" fill="#fff"/><path d="M.5 1l5.5 4 5.5-4" fill="none" stroke="#555"/></svg></span><span>help@vantorinsuranceservice.com</span></div>
  </div>
</div>

<div class="bottombar">
  <span>© Copyright 2025 Vantor Insurance Services. All Rights Reserved</span>
  <nav><span>Terms Privacy</span><span>Support</span></nav>
</div>

</body>
</html>
```